Manual design

Hello,

I am looking for someone creative to help me design my Real Estate related manual. I am looking for something simple yet impressive. It would be designed around my logo and brand colors and I would also like it to have a local feel, perhaps with photos I could provide of my area/hometown. I am really shooting for an impressive company and branded look, while keeping it neat without too much going on.

I have the content that I would like to include, I am just struggling with the design of the manual in general.

I have attached a copy of my logo, my companys logo, and a publisher file of what I had previously done. Please do not think the design I previously used is something to work off of if you deem it better to use another feel. I am looking for originality, unless you can improve upon my old file. Any questions, please feel free to reach out to me.

The content in the provided brochure will remain the same, it is the design aspect I need help with. Thanks

Target Market(s)

My target market is home sellers aged 25-55, people usually selling their 1st or second home

Industry/Entity Type

Real Estate

Requirements
Must have
• -A simple to read design focused around my logo and colors
-A local sense
Should not have
• Drawings, only real photos

```html
<!DOCTYPE html>
<html lang="en">
<head>
<meta charset="utf-8">
<title>Educated Seller's Guide — Colin Ashby</title>
<link href="https://fonts.googleapis.com/css2?family=Didact+Gothic&family=Questrial&family=Montserrat:wght@600;700&display=swap" rel="stylesheet">
<style>
  :root {
    --navy: #0f2557;
    --sky-top: #274a93;
    --sky-mid: #7d9acb;
    --haze: #c7d2e2;
    --water: #2f5a4c;
    --water-deep: #1d3d36;
    --ink: #111111;
    --paper: #ffffff;
    --muted: #c9d2e4;
    --wave: #ececec;
  }
  * { margin: 0; padding: 0; box-sizing: border-box; }
  html, body { width: 1200px; height: 848px; overflow: hidden; background: var(--paper); }
  .spread { position: relative; width: 1200px; height: 848px; font-family: "Didact Gothic", "Questrial", sans-serif; color: var(--ink); }

  /* Cover panel */
  .cover { position: absolute; left: 0; top: 0; width: 592px; height: 848px; overflow: hidden; }
  .cover-photo {
    position: absolute; inset: 0;
    background:
      radial-gradient(ellipse 70% 55% at 0% 0%, rgba(8,18,50,.85), rgba(8,18,50,0) 70%),
      linear-gradient(180deg, var(--sky-top) 0%, var(--sky-mid) 22%, var(--haze) 42%, #9aa7b8 56%, #4f6470 66%, var(--water) 76%, var(--water-deep) 100%);
  }
  .quote {
    position: absolute; left: 32px; top: 538px;
    color: var(--paper); font-size: 20.5px; line-height: 25.2px;
    font-family: "Didact Gothic", sans-serif; word-spacing: 0;
  }
  .quote cite { display: block; font-style: italic; font-family: "Questrial", sans-serif; font-size: 20.5px; }

  .agent-bar {
    position: absolute; left: 0; top: 771px; width: 592px; height: 64px;
    background: var(--navy); color: var(--paper);
  }
  .agent-mark { position: absolute; left: 24px; top: 8px; width: 34px; height: 30px; background: var(--muted); }
  .agent-site { position: absolute; left: 18px; top: 44px; font-size: 11px; letter-spacing: .5px; color: var(--muted); }
  .agent-name { position: absolute; left: 108px; top: 2px; font-family: "Montserrat", sans-serif; font-weight: 700; font-size: 33px; letter-spacing: .3px; }
  .agent-title { position: absolute; left: 109px; top: 44px; font-size: 12px; letter-spacing: .6px; color: var(--muted); }
  .agent-contact { position: absolute; right: 14px; top: 18px; text-align: right; font-style: normal; font-size: 14px; line-height: 21px; letter-spacing: 1.2px; color: var(--muted); }

  /* Contents page */
  .contents { position: absolute; left: 592px; top: 0; width: 608px; height: 848px; }
  .wave-band { position: absolute; left: 0; top: 230px; width: 608px; height: 380px;
    background: linear-gradient(170deg, rgba(255,255,255,0) 20%, var(--wave) 50%, rgba(255,255,255,0) 80%); opacity: .7; }
  .guide-title { position: absolute; left: 29px; top: 42px; font-family: "Questrial", sans-serif; font-weight: 400; font-size: 31px; letter-spacing: .2px; }
  .toc-heading { position: absolute; left: 33px; top: 195px; font-family: "Montserrat", sans-serif; font-weight: 700; font-size: 18px; }
  .toc { position: absolute; left: 33px; top: 229px; width: 535px; list-style: none; }
  .toc li { display: flex; justify-content: space-between; font-size: 17.5px; line-height: 25.1px; word-spacing: 0; }
  .broker { position: absolute; right: 30px; top: 789px; text-align: center; color: var(--navy); font-family: "Montserrat", sans-serif; font-weight: 700; font-size: 19px; line-height: 19px; letter-spacing: .2px; }
</style>
</head>
<body>
<main class="spread">
  <section class="cover">
    <div class="cover-photo" role="img" aria-label="Photograph of a downtown city skyline of high-rise towers beside a harbour with moored boats under a blue sky"></div>
    <blockquote class="quote">
      First comes thought;<br>
      then organization of that thought,<br>
      into ideas and plans;<br>
      then transformation of those plans into reality.<br>
      The beginning, as you will observe,<br>
      is in your imagination.
      <cite>-Marcus Ellery</cite>
    </blockquote>
    <footer class="agent-bar">
      <span class="agent-mark"></span>
      <span class="agent-site">ashby.ca</span>
      <span class="agent-name">Colin Ashby</span>
      <span class="agent-title">Multi-Award Winning Real Estate Professional</span>
      <address class="agent-contact">604-555-0182<br>homes@ashby.ca</address>
    </footer>
  </section>

  <section class="contents">
    <div class="wave-band" role="img" aria-label="Faint flowing line pattern"></div>
    <h1 class="guide-title">Educated Seller's Guide</h1>
    <h2 class="toc-heading">Table of Contents</h2>
    <ol class="toc">
      <li><span>Meet Colin Ashby</span><span>1</span></li>
      <li><span>About Harbourline Realty</span><span>2</span></li>
      <li><span>How to Qualify A Real Estate Professional</span><span>3</span></li>
      <li><span>How I Can Help You</span><span>4,5</span></li>
      <li><span>Where Do Buyers Come From 6</span><span>6</span></li>
      <li><span>Marketing Systems 7,8</span><span>7,8</span></li>
      <li><span>Intelligent Home Pricing 9</span><span>9</span></li>
      <li><span>Your Exclusive Entitlements 10</span><span>12</span></li>
      <li><span>Preparing Your Home for Sale 11</span><span>11</span></li>
      <li><span>Keys to Successful Showings 12</span><span>12</span></li>
      <li><span>Exclusive Easy Exit Guarantee 13</span><span>13</span></li>
      <li><span>A Few Words from Clients 14</span><span>14</span></li>
      <li><span>Forms to Prepare in Advance 15</span><span>15</span></li>
    </ol>
    <div class="broker">HARBOURLINE<br>REALTY</div>
  </section>
</main>
</body>
</html>
```